Design of an attractive membership brochure/membership card for an Electrical Business

Hi, we are an electrical business based in Sydney, Australia.

Our design's aim is to attract and target new customers into using our business as a repeat for anything electrical in their home. We would be handing this out to them after a job is completed and they're happy with the service.
We're thinking of a brochure, possibly additional membership cards with personalized number ID's for each client.

Open to ideas, but some of the things we want to include on our brochure are perks of why the client should sign up with us as a lifetime client
- Discounted emergency call out fees outside of normal hours
- Lifetime membership price, one time payment
- Exclusive 10% member discount on all future jobs
- Priority on any during business hour jobs or emergencies

If any other questions please don't hesitate to reach out.
We've attached our logo for reference for the mock designs.
Our website
https://brightwirecrew.com.au/

```html
<!DOCTYPE html>
<html lang="en">
<head>
<meta charset="utf-8">
<title>Bright Wire Crew – Membership Flyer</title>
<link rel="stylesheet" href="https://fonts.googleapis.com/css2?family=Barlow:wght@300;600;700&family=Nunito:wght@300;400&display=swap">
<style>
  :root {
    --brand-red: #e0332a;
    --deep-red: #a81e1a;
    --ink: #141414;
    --paper: #ffffff;
    --backdrop: #e9e9eb;
    --sky-top: #b9b4cf;
    --house-mid: #56607a;
    --house-dark: #2f3648;
  }
  html, body {
    margin: 0;
    width: 1199px;
    height: 1200px;
    overflow: hidden;
    background: var(--backdrop);
  }
  .flyer {
    position: absolute;
    left: 221px;
    top: 65px;
    width: 756px;
    height: 1069px;
    background: var(--paper);
  }
  .flyer svg { display: block; width: 100%; height: 100%; }
  .brand-name { font-family: "Barlow", sans-serif; font-weight: 700; fill: var(--brand-red); letter-spacing: 1px; }
  .headline-light { font-family: "Barlow", sans-serif; font-weight: 300; fill: var(--paper); }
  .headline-bold { font-family: "Barlow", sans-serif; font-weight: 700; fill: var(--paper); }
  .perk { font-family: "Nunito", sans-serif; font-weight: 300; font-size: 15px; fill: var(--paper); }
  .contact { font-family: "Barlow", sans-serif; font-weight: 300; font-size: 12.5px; fill: var(--paper); }
</style>
</head>
<body>
<main class="flyer">
  <svg viewBox="0 0 605 856" xmlns="http://www.w3.org/2000/svg">
    <defs>
      <linearGradient id="homePhotoTone" x1="0" y1="0" x2="0" y2="1">
        <stop offset="0" stop-color="var(--sky-top)"/>
        <stop offset="0.35" stop-color="var(--house-mid)"/>
        <stop offset="1" stop-color="var(--house-dark)"/>
      </linearGradient>
      <radialGradient id="redGlow" cx="0.3" cy="0.55" r="0.8">
        <stop offset="0" stop-color="var(--brand-red)"/>
        <stop offset="1" stop-color="var(--deep-red)"/>
      </radialGradient>
    </defs>

    <!-- home photo area -->
    <polygon class="home-photo" role="img" aria-label="Photo of a suburban two-storey house with lit windows and a garage at dusk"
      points="378,0 605,0 605,433 320,433 255,213" fill="url(#homePhotoTone)"/>

    <!-- brand name -->
    <text class="brand-name" x="45" y="98" font-size="30">BRIGHT WIRE</text>
    <text class="brand-name" x="45" y="132" font-size="30" letter-spacing="8">CREW</text>

    <!-- headline hexagon -->
    <polygon class="headline-hex" points="0,216 257,216 347,395 257,574 0,574" fill="var(--brand-red)"/>
    <text class="headline-light" x="38" y="333" font-size="33">BRIGHT WIRE</text>
    <text class="headline-bold" x="36" y="405" font-size="66">CREW</text>

    <!-- outline hexagon over photo -->
    <polygon class="outline-hex" points="363,220 513,220 583,348 513,475 363,475 303,348"
      fill="none" stroke="var(--brand-red)" stroke-width="2"/>

    <!-- right red block -->
    <polygon class="accent-block" points="548,450 605,450 605,798 435,798 523,643" fill="url(#redGlow)"/>

    <!-- perks hexagon -->
    <polygon class="perks-hex" points="140,442 410,442 505,640 410,815 140,815 43,640" fill="var(--ink)"/>

    <!-- left outline hexagon -->
    <polygon class="outline-hex-dark" points="0,523 85,523 150,636 85,748 0,748"
      fill="none" stroke="var(--ink)" stroke-width="2"/>

    <g class="perks-list">
      <circle cx="146" cy="545" r="4.5" fill="var(--paper)"/>
      <text class="perk" x="163" y="550">Discounted emergency call out</text>
      <text class="perk" x="163" y="569">fees outside of normal hours</text>

      <circle cx="146" cy="603" r="4.5" fill="var(--paper)"/>
      <text class="perk" x="163" y="608">Lifetime membership price,</text>
      <text class="perk" x="163" y="627">one time payment</text>

      <circle cx="146" cy="662" r="4.5" fill="var(--paper)"/>
      <text class="perk" x="163" y="667">Exclusive 10% member discount</text>
      <text class="perk" x="163" y="686">on all future jobs</text>

      <circle cx="146" cy="720" r="4.5" fill="var(--paper)"/>
      <text class="perk" x="163" y="725">Priority on any during business</text>
      <text class="perk" x="163" y="744">hour jobs or emergencies</text>
    </g>

    <!-- contact band -->
    <rect class="contact-band" x="0" y="815" width="605" height="28" fill="var(--brand-red)"/>
    <g class="contact-icons" fill="var(--paper)" stroke="var(--paper)">
      <path d="M58,824 q-3,3 0,8 l4,4 q5,3 8,0 l-3,-3 -2,1 -4,-4 1,-2 z" stroke="none"/>
      <rect x="175" y="825" width="14" height="10" fill="none" stroke-width="1.3"/>
      <path d="M175,825 l7,6 7,-6" fill="none" stroke-width="1.3"/>
      <circle cx="372" cy="830" r="6.5" fill="none" stroke-width="1.3"/>
      <ellipse cx="372" cy="830" rx="2.8" ry="6.5" fill="none" stroke-width="1.1"/>
      <line x1="365.5" y1="830" x2="378.5" y2="830" stroke-width="1.1"/>
    </g>
    <text class="contact" x="77" y="834.5">102 348 765</text>
    <text class="contact" x="196" y="834.5">info@brightwirecrew.com.au</text>
    <text class="contact" x="386" y="834.5">www.brightwirecrew.com.au</text>
  </svg>
</main>
</body>
</html>
```